Powepoint Templates From Logo

We need 3 Powerpoint templates for use in a variety of presentations we develop and customize. Primary uses of the powerpoint presentations are for printed "pitch books" describing our firm's capabilities and approach (a lot of words with some design elements that we have developed), printed presentations of the results of financial evaluations of our clients (lots of charts and graphs) and as the talking points for speeches.

The design needs to be professional and "solid" to establish that we are capable of selling your multi-million dollar business, but also be a little different to show that we are not just boring MBA's.

Our current website and other materials have been developed internally and leave a great deal to be desired. I have initiated this project to demonstrate how much our look can be improved and, if successful, I hope to do much bigger projects in the future.
Updates

This is my first project and I thaank you all for your participation. Since I am new to this, I don;t know if I am providing the help and feedback as I should. Please feel free to let me know how I can be a better customer.

Target Market(s)

professionals (lawyers, accountaants), business owners, business groups, technology people

Industry/Entity Type

Financial

Requirements
Must have
• our logo
a place where logo of client can be inserted if appropriate
templates for the following pages
title page
standard bullet narrative page
page for charts and graphs to mostly fill the page
Should not have a lot of dark solid color that has to be printed.

Nice to have
• something to perk up the color a little

```html
<!DOCTYPE html>
<html lang="en">
<head>
<meta charset="utf-8">
<title>Title Slide</title>
<link href="https://fonts.googleapis.com/css2?family=Oswald:wght@700&family=Arimo:wght@400;700&display=swap" rel="stylesheet">
<style>
  :root {
    --navy: #0d2f6b;
    --band: #0a2d66;
    --sky-top: #ffffff;
    --sky-soft: #eef3fb;
    --wave-top: #dfe8f5;
    --wave-bottom: #e8eef8;
    --ink: #3a3a3a;
    --photo-a: #8a8f95;
    --photo-b: #3b3e46;
  }
  * { margin: 0; padding: 0; box-sizing: border-box; }
  html, body { width: 1200px; height: 900px; overflow: hidden; background: #fff; }
  .slide {
    position: relative;
    width: 1200px;
    height: 900px;
    overflow: hidden;
    background: linear-gradient(180deg, var(--sky-top) 0%, var(--sky-top) 30%, var(--sky-soft) 60%);
  }
  .top-band {
    position: absolute; left: 0; top: 0; width: 1200px; height: 36px;
    background: var(--band);
    border-bottom: 6px solid #d6e2f2;
  }
  .wave { position: absolute; left: 0; top: 0; width: 1200px; height: 900px; }
  .portrait {
    position: absolute; left: 228px; top: 240px; width: 182px; height: 236px;
    border-radius: 27px;
    background: linear-gradient(160deg, var(--photo-a) 0%, var(--photo-b) 75%);
  }
  .project-title {
    position: absolute; right: 34px; top: 232px;
    font-family: "Oswald", "Arial Narrow", sans-serif;
    font-weight: 700; font-size: 74px; line-height: 1;
    color: var(--navy); letter-spacing: 0.5px;
  }
  .subtitle {
    position: absolute; left: 102px; top: 796px;
    font-family: "Arimo", Arial, sans-serif;
    font-weight: 700; font-size: 38px; color: var(--ink);
  }
  .firm-mark {
    position: absolute; left: 600px; top: 770px;
    display: flex; align-items: center; gap: 18px;
  }
  .firm-mark__square {
    width: 46px; height: 46px; background: var(--navy);
  }
  .firm-mark__name {
    font-family: "Arimo", Arial, sans-serif;
    font-weight: 700; font-size: 50px; color: var(--navy); letter-spacing: 2px;
  }
</style>
</head>
<body>
  <main class="slide">
    <div class="top-band"></div>
    <svg class="wave" viewBox="0 0 1200 900" aria-hidden="true">
      <defs>
        <linearGradient id="waveFill" x1="0" y1="0" x2="0" y2="1">
          <stop offset="0" stop-color="var(--wave-top)"/>
          <stop offset="0.4" stop-color="var(--wave-bottom)"/>
          <stop offset="1" stop-color="#f2f6fc"/>
        </linearGradient>
      </defs>
      <path d="M0 375 C150 470 300 485 500 432 S 820 350 950 356 S 1200 392 1200 392 L1200 900 L0 900 Z" fill="url(#waveFill)"/>
    </svg>
    <div class="portrait" role="img" aria-label="Portrait photo of the presenter"></div>
    <h1 class="project-title">PROJECT TITLE HERE</h1>
    <p class="subtitle">Sub title here</p>
    <div class="firm-mark">
      <span class="firm-mark__square"></span>
      <span class="firm-mark__name">MERIDIAN HOLT</span>
    </div>
  </main>
</body>
</html>
```